Business Cards

We were billed for this because the project timed out. Please give me another designed to open this back up. I was not happy with the last designs (that I was charged for).
we are also using the logo with Revitalizing Pools One Drop at a Time
Also want to utilize Where Healthy Water is our Commitment.

Contact Information for Business Card

Marlowe Stone Group Inc

```html
<!DOCTYPE html>
<html lang="en">
<head>
<meta charset="utf-8">
<title>Marlowe Stone Group – Business Cards</title>
<link href="https://fonts.googleapis.com/css2?family=Arimo:wght@400;700&display=swap" rel="stylesheet">
<style>
  :root {
    --page-bg: #3a3a3a;
    --card-dark: #2a2a2a;
    --card-light: #ffffff;
    --brand-blue: #1f6fbf;
    --ink-dark: #333333;
    --ink-grey: #6b6b6b;
    --rule-grey: #d4d4d4;
    --mark-grey: #8a8a8a;
  }
  * { margin: 0; padding: 0; box-sizing: border-box; }
  html, body { width: 1200px; height: 689px; overflow: hidden; }
  body {
    background: var(--page-bg);
    font-family: "Arimo", Arial, sans-serif;
    display: flex;
    align-items: center;
    justify-content: center;
    gap: 40px;
  }
  .card {
    position: relative;
    width: 540px;
    height: 309px;
    border-radius: 16px;
    overflow: hidden;
  }
  /* Back side */
  .card-back {
    background: var(--card-dark);
    display: flex;
    flex-direction: column;
    align-items: center;
    justify-content: center;
    gap: 22px;
  }
  .card-back .brand-name {
    font-weight: 700;
    font-size: 30px;
    letter-spacing: 2px;
    color: var(--mark-grey);
  }
  .card-back .commitment {
    font-size: 14px;
    color: #f2f2f2;
    letter-spacing: 0.3px;
  }
  /* Front side */
  .card-front { background: var(--card-light); }
  .brand-block {
    position: absolute;
    top: 40px;
    right: 34px;
    text-align: right;
  }
  .brand-block .brand-row {
    display: flex;
    align-items: center;
    justify-content: flex-end;
    gap: 8px;
  }
  .brand-block .brand-square {
    width: 16px; height: 16px;
    background: var(--brand-blue);
  }
  .brand-block .brand-name {
    font-weight: 700;
    font-size: 19px;
    letter-spacing: 1.5px;
    color: var(--ink-dark);
  }
  .brand-block .slogan {
    margin-top: 4px;
    font-size: 8.5px;
    letter-spacing: 1.6px;
    color: var(--ink-dark);
    text-transform: uppercase;
  }
  .divider {
    position: absolute;
    left: 34px; right: 34px;
    top: 128px;
    height: 1px;
    background: var(--rule-grey);
  }
  .address {
    position: absolute;
    top: 144px;
    right: 34px;
    text-align: right;
    font-size: 13px;
    line-height: 1.4;
    color: var(--ink-dark);
  }
  .person {
    position: absolute;
    left: 34px;
    top: 178px;
  }
  .person .name {
    font-size: 20px;
    font-weight: 400;
    color: var(--brand-blue);
    letter-spacing: 0.5px;
  }
  .person .role {
    font-size: 12px;
    color: var(--ink-grey);
    margin-top: 2px;
  }
  .person .rule {
    width: 150px; height: 1px;
    background: var(--rule-grey);
    margin: 8px 0 6px;
  }
  .contacts { list-style: none; }
  .contacts li {
    display: flex;
    align-items: center;
    gap: 8px;
    font-size: 12.5px;
    line-height: 1.35;
    color: var(--ink-dark);
  }
  .contacts svg { width: 10px; height: 10px; fill: var(--brand-blue); flex: none; }
  .band {
    position: absolute;
    left: 0; right: 0; bottom: 0;
    height: 10px;
    background: var(--brand-blue);
    border-top: 3px solid var(--ink-dark);
  }
</style>
</head>
<body>
  <section class="card card-back">
    <div class="brand-name">MARLOWE STONE GROUP</div>
    <p class="commitment">Where Healthy Water is our Commitment</p>
  </section>

  <section class="card card-front">
    <div class="brand-block">
      <div class="brand-row">
        <span class="brand-square"></span>
        <span class="brand-name">MARLOWE STONE GROUP</span>
      </div>
      <div class="slogan">Revitalizing Pools One Drop at a Time</div>
    </div>
    <div class="divider"></div>
    <address class="address" style="font-style:normal">
      412 Alder Court<br>
      Northfield, Canada 20418<br>
      www.marlowestonegroup.com
    </address>
    <div class="person">
      <div class="name">DANIEL REYES</div>
      <div class="role">President</div>
      <div class="rule"></div>
      <ul class="contacts">
        <li><svg viewBox="0 0 10 10"><path d="M2 0 L4 2.5 L3 3.5 Q4.5 6 6.5 7 L7.5 6 L10 8 L8.5 10 Q2 9 0 1.5 Z"/></svg>555-214-7730</li>
        <li><svg viewBox="0 0 10 10"><path d="M2.5 0 H7.5 V10 H2.5 Z M3.5 1 V8 H6.5 V1 Z"/></svg>555-382-9146</li>
        <li><svg viewBox="0 0 10 10"><path d="M0 2 H10 V8 H0 Z M1 3 L5 6 L9 3 Z"/></svg>info@marlowestonegroup.com</li>
      </ul>
    </div>
    <div class="band"></div>
  </section>
</body>
</html>
```